Tech Website

1. Overview
Lumora9, formally named VantoSight, is a pioneer in computer vision technology and machine learning. Based out of Santa Clara, California, Lumora9 is at the forefront of the User Interface revolution; building technology architecture that grants devices with the aptitude to respond to emotional detection, gaze tracking, facial recognition, age and gender identification and gaming interaction. Winner of the Mobile Track at BRISK Founder Sprint 2012, Lumora9 has developed the next generation of consumer behaviour analytics. Lumora9 software solutions are scalable across various platforms including mobile phone, tablets, PC and SmartTV.

Good day, 

Please see the update to our brief - there is a PDF of the type of format and design we are looking for.  It shows each page - Landing, Technology, Product, Press and Company.

Thank you for your designs

Regards,

Target Market(s)

Target market - A mix of enterprise and consumer audiences, targeting the need for the technology in the living room space

Industry/Entity Type

Architecture

Requirements
Must have
• Design preferences - Easy to navigate, modern with sleek feel, trendy, tech saavy, using cube as a consistent element/theme. colours are not determined, but parrot green was one idea with 2 additional underlying colours. keys words like user interface revolution or sense recognition are good sources to draw inspiration.

Landing page will have a video - illustrating different uses of technology

Technical Specs - Landing page, 6 tabs/subpages, and each subpage may have 1 or 2 additional pages. Coding will be necessary, not that much at the beginning stages.

```html
<!DOCTYPE html>
<html lang="en">
<head>
<meta charset="utf-8">
<title>Lumora9</title>
<link rel="stylesheet" href="https://fonts.googleapis.com/css2?family=Oswald:wght@400;500&family=Ubuntu:wght@400;500;700&family=Arimo&display=swap">
<style>
:root{
  --green-dark:#4a7a26;
  --green-mid:#5f8f34;
  --parrot:#6cb61a;
  --parrot-light:#8fd246;
  --nav-dark:#17181a;
  --nav-mid:#2c2e31;
  --panel:#efefef;
  --ink:#3a3a3a;
  --body:#555;
  --link:#2f7d12;
  --white:#fff;
}
*{margin:0;padding:0;box-sizing:border-box}
html,body{width:938px;height:1200px;overflow:hidden;background:var(--panel)}
.page{position:relative;width:938px;height:1200px;font-family:"Arimo",sans-serif;color:var(--body)}
.abs{position:absolute}

.masthead{left:0;top:0;width:938px;height:82px;background:linear-gradient(var(--green-mid),var(--green-dark))}
.brand{left:94px;top:20px;display:flex;align-items:center;gap:16px}
.brand-mark{width:36px;height:36px;background:var(--white)}
.brand-name{font-family:"Ubuntu",sans-serif;font-size:44px;font-weight:400;color:var(--white);line-height:1}
.pill{left:674px;width:132px;height:23px;border-radius:4px;background:linear-gradient(#333,#0d0d0d);box-shadow:0 3px 6px rgba(0,0,0,.45);font-family:"Ubuntu",sans-serif;font-size:8px;font-weight:500;color:var(--white);display:flex;align-items:center;justify-content:center}

.navbar{left:0;top:82px;width:938px;height:39px;background:linear-gradient(var(--nav-mid),var(--nav-dark))}
.nav-links{left:99px;top:0;height:39px;display:flex;gap:22px;align-items:center;list-style:none}
.nav-links li{font-family:"Oswald",sans-serif;font-size:13px;color:var(--white);letter-spacing:.2px}
.social{top:13px;width:13px;height:13px;border-radius:50%;background:#9a9a9a}

.hero{left:0;top:121px;width:938px;height:353px;background:radial-gradient(ellipse at 50% 40%,var(--parrot-light) 0%,var(--parrot) 45%,#5aa010 100%)}
.hero-white{left:0;top:474px;width:938px;height:90px;background:var(--white)}
.laptop-lid{left:221px;top:157px;width:491px;height:336px;background:#0c0c0c;border-radius:8px 8px 0 0;border:2px solid #9a9a9a;border-bottom:none}
.laptop-screen{left:239px;top:179px;width:454px;height:295px;background:linear-gradient(#1f2d63 0%,#3a4d86 45%,#6b5f6e 80%,#2c2a24 100%)}
.laptop-base{left:137px;top:493px;width:657px;height:31px;border-radius:2px 2px 14px 14px;background:linear-gradient(#f4f4f4,#c9c9c9 60%,#9d9d9d)}
.dot{top:497px;width:10px;height:10px;border-radius:50%;background:#ddd;border:1px solid #aaa}
.dot.on{background:var(--parrot);border-color:#4c8a0e}
.arrow{top:305px;width:42px;height:42px}

.feature{top:590px;width:240px}
.feature h2{font-family:"Oswald",sans-serif;font-weight:400;font-size:21px;color:var(--ink);display:flex;align-items:center;gap:6px}
.feature p{margin-top:14px;font-size:9.6px;line-height:14px;color:var(--body)}

.showcase{left:99px;top:717px;width:734px;height:281px;background:#ececec;border:1px solid #c8c8c8;box-shadow:0 4px 8px rgba(0,0,0,.12)}
.divider{top:0;width:1px;height:279px;background:#d2d2d2}
.card{top:0;width:230px}
.card h3{margin-top:18px;font-family:"Oswald",sans-serif;font-weight:400;font-size:20px;color:#7c7c7c}
.card-media{margin-top:11px;width:203px;height:90px;border-radius:3px;box-shadow:0 2px 4px rgba(0,0,0,.35);position:relative}
.play-sm{position:absolute;left:50%;top:50%;width:28px;height:18px;margin:-9px 0 0 -14px;background:#0f6a1e}
.card p{font-family:"Ubuntu",sans-serif;font-size:9px;line-height:14px;color:#666;margin-top:14px;padding-left:2px}
.card p+p{margin-top:14px}
.card a{color:var(--link);font-weight:700;text-decoration:underline}

.press{top:1030px;width:134px;height:88px;background:linear-gradient(#fff,#f1f1f1);border:1px solid #cfcfcf;box-shadow:0 8px 8px -4px rgba(0,0,0,.25);display:flex;align-items:center;justify-content:center;font-family:"Oswald",sans-serif;font-size:22px;font-weight:500;color:#555}

.footer{left:0;top:1144px;width:938px;height:56px;background:linear-gradient(var(--green-mid),var(--green-dark))}
.footer p{position:absolute;left:0;width:100%;top:27px;text-align:center;font-family:"Ubuntu",sans-serif;font-size:8px;color:#1d2a0f}
</style>
</head>
<body>
<div class="page">

  <header class="masthead abs">
    <div class="brand abs"><span class="brand-mark"></span><span class="brand-name">Lumora9</span></div>
    <div class="pill abs" style="top:13px">Join Us At: Nexcon 2013 Jan 8-11</div>
    <div class="pill abs" style="top:46px">Subscribe to LUMORA9 Blog</div>
  </header>

  <nav class="navbar abs">
    <ul class="nav-links abs">
      <li>HOME</li><li>TECHNOLOGY</li><li>PRODUCT</li><li>PRESS</li><li>CONTACT</li>
    </ul>
    <span class="social abs" style="left:746px"></span>
    <span class="social abs" style="left:771px"></span>
    <span class="social abs" style="left:796px"></span>
    <span class="social abs" style="left:820px"></span>
  </nav>

  <section class="hero abs"></section>
  <div class="hero-white abs"></div>

  <div class="laptop-lid abs"></div>
  <div class="laptop-screen abs" role="img" aria-label="Video still of a lattice-shell building at dusk with palm trees"></div>
  <svg class="abs" style="left:436px;top:307px" width="58" height="38" viewBox="0 0 58 38">
    <rect width="58" height="38" fill="#222" opacity=".85"/>
    <polygon points="23,9 23,29 38,19" fill="#fff"/>
  </svg>
  <div class="laptop-base abs"></div>
  <svg class="abs" style="left:742px;top:500px" width="20" height="3"><rect width="20" height="2" fill="#555"/></svg>
  <span class="dot abs" style="left:417px"></span>
  <span class="dot on abs" style="left:440px"></span>
  <span class="dot abs" style="left:461px"></span>
  <span class="dot abs" style="left:484px"></span>
  <span class="dot abs" style="left:505px"></span>

  <svg class="arrow abs" style="left:163px" viewBox="0 0 42 42">
    <circle cx="21" cy="21" r="20" fill="#1b1b1b"/><circle cx="21" cy="21" r="14" fill="#fff"/>
    <polygon points="15,21 25,14 25,28" fill="#1b1b1b"/>
  </svg>
  <svg class="arrow abs" style="left:726px" viewBox="0 0 42 42">
    <circle cx="21" cy="21" r="20" fill="#1b1b1b"/><circle cx="21" cy="21" r="14" fill="#fff"/>
    <polygon points="27,21 17,14 17,28" fill="#1b1b1b"/>
  </svg>

  <section class="feature abs" style="left:99px">
    <h2><svg width="18" height="18" viewBox="0 0 18 18"><g fill="none" stroke="#333" stroke-width="2.4"><rect x="8" y="2" width="8" height="5" rx="2.5" transform="rotate(-45 12 4.5)"/><rect x="2" y="11" width="8" height="5" rx="2.5" transform="rotate(-45 6 13.5)"/></g></svg>Mobile Applications</h2>
    <p>Lorem ipsum dolor sit amet, consectetur adipiscing elit. Sed consequat mollis eros dictum tempor. Donec ornare turpis in nisi condimentum a accumsan massa auctor.</p>
  </section>
  <section class="feature abs" style="left:349px">
    <h2><svg width="18" height="18" viewBox="0 0 18 18"><path d="M3 14c3 3 7 2 7-1l-2-2-2 1c-1-1-2-2-2-4l1-2-2-2C0 4-1 9 3 14z" transform="translate(3 -1) rotate(10 9 9)" fill="#333"/></svg>Smart Phone Applications</h2>
    <p>Lorem ipsum dolor sit amet, consectetur adipiscing elit. Sed consequat mollis eros dictum tempor. Donec ornare turpis in nisi condimentum a accumsan massa auctor.</p>
  </section>
  <section class="feature abs" style="left:598px">
    <h2><svg width="18" height="18" viewBox="0 0 18 18"><path d="M2 16l1-5 9-9 4 4-9 9z" fill="#333"/></svg>Smart TV Softwares</h2>
    <p>Lorem ipsum dolor sit amet, consectetur adipiscing elit. Sed consequat mollis eros dictum tempor. Donec ornare turpis in nisi condimentum a accumsan massa auctor.</p>
  </section>

  <section class="showcase abs">
    <span class="divider abs" style="left:241px"></span>
    <span class="divider abs" style="left:490px"></span>

    <article class="card abs" style="left:15px">
      <h3>Tablet Pc</h3>
      <div class="card-media" role="img" aria-label="Tablet showing an app home screen" style="background:linear-gradient(#2a2a2a,#3c3c3c)"><span class="play-sm"></span></div>
      <p>Proin eget orci a nulla consequat hendrerit. Nunc non dictum quam. Nam sed est non est imperdiet faucibus a vitae mauris.</p>
      <p>Suspendisse tincidunt, nunc nec porttitor molestie, sapien sem convallis erat, at faucibus diam neque eu tortor... <a>Read More</a></p>
    </article>
    <article class="card abs" style="left:265px">
      <h3>Mobile</h3>
      <div class="card-media" role="img" aria-label="Slider phone with keyboard" style="background:linear-gradient(#5a5a5a,#4a4a4a)"><span class="play-sm"></span></div>
      <p>Proin eget orci a nulla consequat hendrerit. Nunc non dictum quam. Nam sed est non est imperdiet faucibus a vitae mauris.</p>
      <p>Suspendisse tincidunt, nunc nec porttitor molestie, sapien sem convallis erat, at faucibus diam neque eu tortor... <a>Read More</a></p>
    </article>
    <article class="card abs" style="left:510px">
      <h3>Smart TV</h3>
      <div class="card-media" role="img" aria-label="Flat screen television showing a media app" style="background:linear-gradient(#5a5a5a,#454545)"><span class="play-sm"></span></div>
      <p>Proin eget orci a nulla consequat hendrerit. Nunc non dictum quam. Nam sed est non est imperdiet faucibus a vitae mauris.</p>
      <p>Suspendisse tincidunt, nunc nec porttitor molestie, sapien sem convallis erat, at faucibus diam neque eu tortor... <a>Read More</a></p>
    </article>
  </section>

  <div class="press abs" style="left:100px">Yondra</div>
  <div class="press abs" style="left:253px">Flashwire</div>
  <div class="press abs" style="left:402px">KVN</div>
  <div class="press abs" style="left:549px;font-size:18px">Gadget Ledger</div>
  <div class="press abs" style="left:694px">Norvale</div>

  <footer class="footer abs"><p>Copyright © 2012 Lumora9. All rights reserved.</p></footer>
</div>
</body>
</html>
```